Business Card Design Project

Use our current logo. Clean design.

Industry/Entity Type

Business

Requirements
Must have
• Marisela DUBRANCQ
M. Law
Managing Partner

Alpenvorsa AG
Kornhalmweg 214
CH-3097 Liebefeld

M. +41 79 412 56 27
T. +41 31 928 44 10
F. +41 31 928 44 19

m.dubrancq@alpenvorsa-example.com
www.alpenvorsa-example.com

```html
<!DOCTYPE html>
<html lang="en">
<head>
<meta charset="utf-8">
<title>Alpenvorsa AG – Business Card</title>
<link href="https://fonts.googleapis.com/css2?family=Tenor+Sans&family=Mulish:wght@400;700;800&display=swap" rel="stylesheet">
<style>
  :root {
    --backdrop: #161616;
    --card-white: #ffffff;
    --card-dark-top: #5a5a5a;
    --card-dark-bottom: #2e2e2e;
    --ink: #1c1c1c;
    --ink-soft: #3a3a3a;
    --rule: #2a2a2a;
    --brand-light: #e6e6e6;
  }
  * { box-sizing: border-box; margin: 0; padding: 0; }
  html, body {
    width: 1200px; height: 871px; overflow: hidden;
    background: var(--backdrop);
  }
  .stage {
    width: 1200px; height: 871px;
    display: flex; align-items: center; justify-content: center; gap: 50px;
  }
  .card {
    width: 540px; height: 340px; position: relative;
    box-shadow: 0 12px 30px rgba(0,0,0,.6);
  }
  /* Back side */
  .card--back {
    background: linear-gradient(160deg, var(--card-dark-top), var(--card-dark-bottom));
    display: flex; align-items: center; justify-content: center;
  }
  .back-brand {
    font-family: "Tenor Sans", sans-serif;
    font-size: 40px; letter-spacing: 2px;
    color: var(--brand-light);
  }
  /* Front side */
  .card--front { background: var(--card-white); color: var(--ink); }
  .front-brand {
    position: absolute; left: 38px; top: 38px;
    font-family: "Tenor Sans", sans-serif;
    font-size: 30px; letter-spacing: .5px; color: var(--ink);
  }
  .rule-main {
    position: absolute; left: 22px; right: 30px; top: 196px;
    border-top: 1px solid var(--rule);
  }
  .rule-minor {
    position: absolute; left: 300px; right: 30px; top: 248px;
    border-top: 1px solid var(--rule);
  }
  .contacts {
    position: absolute; left: 30px; top: 210px;
    font-family: "Mulish", sans-serif; font-size: 13px; line-height: 20px;
    color: var(--ink);
    display: grid; grid-template-columns: 24px auto;
  }
  .contacts dt { font-weight: 800; }
  .contacts .email { grid-column: 1 / 3; padding-left: 0; }
  .person {
    position: absolute; right: 30px; top: 174px; text-align: right;
    font-family: "Mulish", sans-serif; color: var(--ink);
  }
  .person-name { font-size: 14px; font-weight: 800; line-height: 20px; }
  .person-role { font-size: 14px; font-weight: 400; line-height: 20px; margin-top: 6px; color: var(--ink-soft); }
  .company {
    position: absolute; right: 30px; top: 262px; text-align: right;
    font-family: "Mulish", sans-serif; font-size: 14px; line-height: 20px; color: var(--ink-soft);
  }
  .company-name { font-weight: 800; color: var(--ink); }
</style>
</head>
<body>
  <main class="stage">
    <section class="card card--back" aria-label="Card back">
      <div class="back-brand">ALPENVORSA</div>
    </section>

    <section class="card card--front" aria-label="Card front">
      <div class="front-brand">ALPENVORSA</div>

      <div class="rule-main"></div>

      <dl class="contacts">
        <dt>M.</dt><dd>+41 79 412 56 27</dd>
        <dt>T.</dt><dd>+41 31 928 44 10</dd>
        <dt>F.</dt><dd>+41 31 928 44 19</dd>
        <dt>E.</dt><dd>m.dubrancq@alpenvorsa-example.com</dd>
      </dl>

      <div class="person">
        <div class="person-name">Marisela DUBRANCQ M. Law</div>
        <div class="person-role">Managing Partner</div>
      </div>

      <div class="rule-minor"></div>

      <address class="company" style="font-style:normal">
        <div class="company-name">Alpenvorsa AG</div>
        <div>Kornhalmweg 214</div>
        <div>CH-3097 Liebefeld</div>
      </address>
    </section>
  </main>
</body>
</html>
```